Water bottle logo and other essentials and accessories

Hello,

We have an exclusive villa in Italy where our guests get free water from our bottles as a courtesy. (as well as wine, beer etc)

We ordered 1000 bottles and it seems like we can have our Logo and/or house name on the bottles.

Well.. we have a house name( Villa Serena), but not a logo.

If the bottle Logo ends good we will continue to use the logo in the future.

The Villa is high end, by the mediterranean sea.

Target Market(s)

High end travelers

Industry/Entity Type

Real Estate

Font styles to use
Decorative
Script

Colors

Designer to choose colors to be used in the design.

Requirements
Must have
• Class
Nice to have
• Imagine "Kelda Water".
Should not have
• Tropical colors
• Hello, I like your idea here.
• Just to be precise: The Kelda water picture I added is just for inspiration.
• If possible you can write:
• Acqua Minerale and Acqua Frizzante instead

```html
<!DOCTYPE html>
<html lang="en">
<head>
<meta charset="utf-8">
<title>Villa Serena – Acqua Frizzante label</title>
<link href="https://fonts.googleapis.com/css2?family=Cinzel+Decorative&family=Lato:wght@300;400&display=swap" rel="stylesheet">
<style>
  :root {
    --label-black: #000000;
    --ivory: #ffffff;
    --gold: #d9b24f;
    --gold-deep: #b8923a;
  }
  html, body {
    margin: 0;
    padding: 0;
    background: var(--label-black);
    overflow: hidden;
  }
  .label {
    position: relative;
    width: 1200px;
    height: 892px;
    background: var(--label-black);
    overflow: hidden;
    color: var(--ivory);
  }
  .ornament {
    position: absolute;
    width: 398px;
    height: 202px;
  }
  .ornament--top {
    left: 400px;
    top: 94px;
    background: linear-gradient(180deg, var(--gold) 0%, var(--gold-deep) 100%);
    clip-path: polygon(50% 0, 62% 40%, 100% 128px, 100% 100%, 0 100%, 0 128px, 38% 40%);
  }
  .ornament--bottom {
    left: 404px;
    top: 436px;
    background: linear-gradient(0deg, var(--gold) 0%, var(--gold-deep) 100%);
    clip-path: polygon(0 0, 100% 0, 100% 74px, 62% 60%, 50% 100%, 38% 60%, 0 74px);
  }
  .house-name {
    position: absolute;
    top: 338px;
    left: 0;
    width: 1200px;
    margin: 0;
    text-align: center;
    font-family: "Cinzel Decorative", "Cinzel", serif;
    font-weight: 400;
    font-size: 80px;
    line-height: 1.1;
    letter-spacing: 1px;
    color: var(--ivory);
  }
  .variety {
    position: absolute;
    top: 736px;
    left: 0;
    width: 1200px;
    margin: 0;
    text-align: center;
    font-family: "Lato", sans-serif;
    font-weight: 400;
    font-size: 36px;
    color: var(--ivory);
  }
  .contact {
    position: absolute;
    top: 322px;
    left: 42px;
    height: 248px;
    writing-mode: vertical-rl;
    text-align: center;
    font-family: "Lato", sans-serif;
    font-weight: 400;
    font-size: 23px;
    line-height: 22px;
    color: var(--ivory);
  }
  .contact span { display: block; }
  .website {
    position: absolute;
    top: 302px;
    left: 1124px;
    height: 284px;
    writing-mode: vertical-rl;
    transform: rotate(180deg);
    text-align: center;
    font-family: "Lato", sans-serif;
    font-weight: 300;
    font-size: 32px;
    line-height: 30px;
    color: var(--ivory);
  }
</style>
</head>
<body>
  <main class="label">
    <div class="ornament ornament--top" role="img" aria-label="Gold filigree flourish ornament above the house name"></div>

    <h1 class="house-name">Villa Serena</h1>

    <div class="ornament ornament--bottom" role="img" aria-label="Mirrored gold filigree flourish ornament below the house name"></div>

    <p class="variety">Acqua Frizzante</p>

    <div class="contact">
      <span class="email">hello@villaserena.it</span>
      <span class="phone">+47 91234567</span>
    </div>

    <div class="website">www.villaserena.no</div>
  </main>
</body>
</html>
```